VENTURE CAPITAL GROUP BUSINESS CARD DESIGN

Venture Capital Group based in SF looking for a bold business card design. No trendy colour explosion, 3D effects etc. Just "simple" optical effects. Works on your brain, keeps your eye focused and sticks to your mind.
Target Market(s)
Technology startups
Industry/Entity Type
Venture Capital
Contact Information for Business Card
BARNABY WHITLOCK
MANAGING PARTNER
817 FERN ST SAN FRANCISCO, CA 94111
415.555.0143 O
415.555.0167 F
415.555.0192 C
barn@halcyonridgefund.example

```html
<!DOCTYPE html>
<html lang="en">
<head>
<meta charset="utf-8">
<title>Halcyon Ridge Capital Group — Business Card</title>
<link rel="stylesheet" href="https://fonts.googleapis.com/css2?family=Open+Sans:wght@400;600;700&display=swap">
<style>
  :root {
    --backdrop: #2b2b2b;
    --card: #050505;
    --card-edge: #0f1410;
    --green: #1f9a3a;
    --green-bright: #2fb84a;
    --white: #f4f4f4;
    --muted: #d9d9d9;
    --mark: #e6e6e6;
    --divider: #3a3a3a;
  }
  * { margin: 0; padding: 0; box-sizing: border-box; }
  html, body { width: 1200px; height: 900px; overflow: hidden; }
  body {
    background: var(--backdrop);
    font-family: "Open Sans", Arial, sans-serif;
    position: relative;
  }
  .card {
    position: absolute;
    width: 600px;
    height: 343px;
    border-radius: 22px;
    background: var(--card);
    box-shadow: 0 18px 40px rgba(0,0,0,.55);
    overflow: hidden;
  }
  .card--front { left: 110px; top: 80px; }
  .card--back {
    left: 490px; top: 470px;
    background: linear-gradient(120deg, #0a120c 0%, var(--card) 55%, var(--card) 100%);
  }

  .brand {
    display: flex;
    flex-direction: column;
    align-items: center;
    gap: 16px;
  }
  .brand__circle {
    width: 92px; height: 92px;
    border-radius: 50%;
    background: radial-gradient(circle at 40% 35%, #ffffff 0%, var(--mark) 70%, #bdbdbd 100%);
  }
  .brand__name {
    color: var(--green);
    font-weight: 600;
    font-size: 22px;
    letter-spacing: 2px;
    text-align: center;
    line-height: 1.25;
    text-transform: uppercase;
  }
  .card--front .brand {
    position: absolute;
    left: 0; right: 0; top: 72px;
  }

  .card--back .brand {
    position: absolute;
    left: 40px; top: 88px;
    width: 230px;
    gap: 14px;
  }
  .card--back .brand__circle { width: 80px; height: 80px; }
  .card--back .brand__name { font-size: 17px; }

  .divider {
    position: absolute;
    left: 292px; top: 60px;
    width: 1px; height: 200px;
    background: var(--divider);
  }

  .contact {
    position: absolute;
    left: 314px; top: 58px;
    right: 20px;
    color: var(--muted);
  }
  .contact__name {
    color: var(--white);
    font-weight: 700;
    font-size: 22px;
    letter-spacing: .5px;
    line-height: 1.1;
  }
  .contact__title {
    color: var(--green-bright);
    font-weight: 600;
    font-size: 12px;
    letter-spacing: 1px;
    margin-top: 4px;
  }
  .contact__address {
    font-size: 12px;
    letter-spacing: .6px;
    line-height: 1.35;
    margin-top: 12px;
    text-transform: uppercase;
  }
  .contact__list { list-style: none; margin-top: 8px; }
  .contact__item {
    display: flex;
    align-items: center;
    gap: 8px;
    font-size: 12.5px;
    line-height: 1.5;
    letter-spacing: .4px;
  }
  .contact__icon { width: 11px; height: 11px; flex: none; }
  .contact__icon * { fill: none; stroke: var(--green-bright); stroke-width: 1.6; stroke-linecap: round; stroke-linejoin: round; }
</style>
</head>
<body>

<section class="card card--front" aria-label="Card front">
  <div class="brand">
    <div class="brand__circle"></div>
    <p class="brand__name">Halcyon Ridge<br>Capital Group</p>
  </div>
</section>

<section class="card card--back" aria-label="Card back">
  <div class="brand">
    <div class="brand__circle"></div>
    <p class="brand__name">Halcyon Ridge<br>Capital Group</p>
  </div>

  <div class="divider"></div>

  <div class="contact">
    <h1 class="contact__name">BARNABY WHITLOCK</h1>
    <p class="contact__title">MANAGING PARTNER</p>
    <p class="contact__address">817 Fern St San<br>Francisco, CA 94111</p>
    <ul class="contact__list">
      <li class="contact__item">
        <svg class="contact__icon" viewBox="0 0 12 12" aria-hidden="true"><path d="M2 1.5l2 .3.8 2.3-1.3 1a6 6 0 0 0 3.4 3.4l1-1.3 2.3.8.3 2c-5 .6-9-3.4-8.5-8.5z"/></svg>
        <span>415.555.0143</span>
      </li>
      <li class="contact__item">
        <svg class="contact__icon" viewBox="0 0 12 12" aria-hidden="true"><rect x="3" y="1" width="6" height="3"/><rect x="1" y="4" width="10" height="5"/><rect x="3" y="7.5" width="6" height="3.5"/></svg>
        <span>415.555.0167</span>
      </li>
      <li class="contact__item">
        <svg class="contact__icon" viewBox="0 0 12 12" aria-hidden="true"><rect x="3" y="1" width="6" height="10" rx="1"/><path d="M5.5 9h1"/></svg>
        <span>415.555.0192</span>
      </li>
      <li class="contact__item">
        <svg class="contact__icon" viewBox="0 0 12 12" aria-hidden="true"><rect x="1" y="2.5" width="10" height="7"/><path d="M1 2.5l5 4 5-4"/></svg>
        <span>barn@halcyonridgefund.example</span>
      </li>
    </ul>
  </div>
</section>

</body>
</html>
```